The Truths About Child Neglect

The goal of this info-graphic is to visually command the attention of our intended audience (teen/adult parents, teachers, youth program coordinators, etc.). Because this project has to do with children, the design should have pops of color; it should be an info-graphic that schools and non profit youth organizations would gladly welcome as an addition to their website. It is important though that the aesthetic, while stimulating the viewer, doesn't overpower the information. The final design should ultimately highlight the innocence of childhood.

Note: the information that has been uploaded is currently formatted in a mock-up info-graphic. Please do not follow that aesthetic; the above description is the route that we would like to take things.

Target Market(s)

Parents
Teachers
Youth Organizations
Parent Bloggers

Industry/Entity Type

Childcare

Font styles to use
Serif
Decorative

Colors

Designer to choose colors to be used in the design.

Requirements
Must have
• Visually captivating imagery
• The info-graphic should grab the viewers attention.
• Sources must be sited at the bottom in small print.
• Looks professional
Nice to have
• A story telling flow of imagery within the info-graphic, which makes it easier for viewers to follow the poignant details.
Should not have
• Boring imagery.
• Heavy text/too much wording.
• Lack of sited sources.

```html
<!DOCTYPE html>
<html lang="en">
<head>
<meta charset="utf-8">
<title>The Truths About Child Neglect</title>
<link rel="stylesheet" href="https://fonts.googleapis.com/css2?family=Oswald:wght@600&family=Roboto+Condensed:wght@500;700&family=Cabin+Sketch:wght@700&display=swap">
<style>
  :root {
    --cyan: #4ee8e0;
    --ink: #222226;
    --orange: #f3511f;
    --lime: #c6f21a;
    --lime-deep: #b5ec12;
    --cream: #f2f1de;
    --text: #2a2a28;
    --chalk: #f4f4f0;
    --board-1: #2b2c2e;
    --board-2: #3d3e40;
    --red: #ef2f3b;
  }
  * { margin: 0; padding: 0; box-sizing: border-box; }
  html, body { width: 848px; height: 1200px; overflow: hidden; background: #fff; }
  .infographic { position: relative; width: 848px; height: 1200px; overflow: hidden; font-family: "Roboto Condensed", Arial, sans-serif; }

  .title-band { position: absolute; left: 0; top: 0; width: 848px; height: 104px; background: var(--cyan); }
  .title-pill {
    position: absolute; left: 36px; top: 22px; width: 770px; height: 64px;
    background: var(--ink); border-radius: 32px;
    display: flex; align-items: center; justify-content: center;
  }
  .title-pill h1 { font-family: "Oswald", Impact, sans-serif; font-weight: 600; font-size: 40px; letter-spacing: 1px; color: var(--orange); }

  .chalkboard { position: absolute; left: 0; width: 848px; background: radial-gradient(ellipse at 55% 45%, var(--board-2), var(--board-1) 75%); }
  .board-ways { top: 104px; height: 228px; }
  .board-consequences { top: 672px; height: 194px; }
  .chalk-heading {
    position: absolute; z-index: 2;
    font-family: "Cabin Sketch", "Comic Sans MS", cursive; font-weight: 700;
    color: var(--chalk); white-space: nowrap;
  }
  .board-ways .chalk-heading { left: 226px; top: 14px; font-size: 42px; line-height: 68px; }
  .board-consequences .chalk-heading { left: 212px; top: 34px; font-size: 40px; line-height: 68px; }
  .art { position: absolute; border-radius: 6px; background: linear-gradient(160deg, #4a4b4e, #353638); }
  .art-parents { left: 0; top: 20px; width: 212px; height: 208px; }
  .art-kids { left: 678px; top: 100px; width: 160px; height: 124px; }
  .art-jailed { left: 0; top: 10px; width: 176px; height: 184px; }
  .art-wordcloud { left: 660px; top: 0; width: 188px; height: 194px; }

  .ways-section {
    position: absolute; left: 0; top: 332px; width: 848px; height: 340px;
    background: linear-gradient(180deg, #7ff0b8 0%, var(--lime) 28%, var(--lime-deep) 100%);
  }
  .way {
    position: absolute; height: 60px; background: var(--cream);
    display: flex; align-items: center; padding: 0 20px;
    font-size: 14px; font-weight: 700; line-height: 19px; color: var(--text);
    text-transform: uppercase; white-space: nowrap;
  }
  .way.left { left: 0; width: 404px; border-radius: 0 30px 30px 0; }
  .way.right { left: 442px; width: 406px; border-radius: 30px 0 0 30px; padding-left: 42px; }

  .consequences-section {
    position: absolute; left: 0; top: 866px; width: 848px; height: 334px;
    background: linear-gradient(180deg, var(--lime) 0%, #f2c21a 42%, var(--orange) 72%, var(--red) 100%);
  }
  .consequence {
    position: absolute; height: 54px; background: var(--cream);
    box-shadow: 4px 5px 0 rgba(0,0,0,0.12);
    display: flex; align-items: center; padding-left: 28px;
    font-size: 14px; font-weight: 700; color: var(--text);
    text-transform: uppercase; white-space: nowrap;
  }
  .consequence::before {
    content: ""; position: absolute; left: -6px; top: -8px; width: 40px; height: 30px;
    background: var(--cyan); clip-path: polygon(0 0, 100% 0, 0 100%);
  }
  .consequence .num { position: absolute; left: 2px; top: -6px; font-size: 14px; font-weight: 700; z-index: 1; }
  .sources {
    position: absolute; right: 16px; bottom: 8px;
    font-size: 9px; font-weight: 500; color: #fff; letter-spacing: 0.2px;
  }
</style>
</head>
<body>
<main class="infographic">
  <header class="title-band">
    <div class="title-pill"><h1>THE TRUTHS ABOUT CHILD NEGLECT</h1></div>
  </header>

  <section class="chalkboard board-ways">
    <div class="art art-parents" role="img" aria-label="Chalk drawing of two worried parents"></div>
    <div class="art art-kids" role="img" aria-label="Chalk drawing of three smiling children"></div>
    <h2 class="chalk-heading">8 DIFFERENT WAYS<br>YOU CAN BE CHARGED<br>WITH CHILD NEGLECT</h2>
  </section>

  <section class="ways-section">
    <p class="way left" style="top:32px">Leaving your child to play outside by themselves,<br>whether they are on your property or not.</p>
    <p class="way left" style="top:104px">Leaving your child in the car unsupervised,<br>despite the length of time they are left alone.</p>
    <p class="way left" style="top:176px">Leaving your child home alone without arranging<br>for reasonable care or supervision.</p>
    <p class="way left" style="top:248px">Becoming emotionally or physically combative<br>with the other parent while your child is present.</p>
    <p class="way right" style="top:32px">Failing to provide your child with regular<br>medical attention, despite your income.</p>
    <p class="way right" style="top:104px">Failing to give your child adequate attention,<br>regardless of your time constraints, and<br>refusing help from others.</p>
    <p class="way right" style="top:176px">Allowing your child to wear clothes that are<br>deemed inappropriate for the weather,<br>their age, etc.</p>
    <p class="way right" style="top:248px">Not being present if/when your child<br>throws a party in your home.</p>
  </section>

  <section class="chalkboard board-consequences">
    <div class="art art-jailed" role="img" aria-label="Chalk drawing of a worried man behind bars"></div>
    <div class="art art-wordcloud" role="img" aria-label="Chalk drawing of a figure under a cloud of words like jail, fines and parental rights"></div>
    <h2 class="chalk-heading">7 CONSEQUENCES OF A<br>CHILD NEGLECT CHARGE</h2>
  </section>

  <section class="consequences-section">
    <p class="consequence" style="left:22px;top:20px;width:120px"><span class="num">1.</span>Jail time.</p>
    <p class="consequence" style="left:22px;top:90px;width:346px"><span class="num">2.</span>The loss of custody or parental rights.</p>
    <p class="consequence" style="left:22px;top:158px;width:104px"><span class="num">3.</span>Fines.</p>
    <p class="consequence" style="left:22px;top:236px;width:136px"><span class="num">4.</span>An injunction.</p>
    <p class="consequence" style="left:414px;top:20px;width:346px"><span class="num">5.</span>Registration as a sex offender.</p>
    <p class="consequence" style="left:414px;top:90px;width:346px"><span class="num">6.</span>Restrictions on probation and parole.</p>
    <p class="consequence" style="left:414px;top:158px;width:410px"><span class="num">7.</span>Involuntary commitment to a mental institution.</p>
    <p class="sources">Sources: state child welfare statutes; family court guidance on child neglect.</p>
  </section>
</main>
</body>
</html>
```